Webdesign für Brandt Maler
Zielgruppe
Maler- und Bodenlegerarbeiten, Farbenherstellung, Fachmarkt
ZieIgruppe sind alle, die Fraben und/oder die Dienstleistungen der Firma benötigen
Aufgabenstellung
dem Kunde gefällt die Seite http://www.maler-quirinus.example/
bitte alle Uploads beachten
eigene Bilder und Stockmaterial

```html
<!DOCTYPE html>
<html lang="de">
<head>
<meta charset="utf-8">
<title>Brandt Maler</title>
<link rel="stylesheet" href="https://fonts.googleapis.com/css2?family=Varela+Round&family=Open+Sans:wght@400;600&display=swap">
<style>
  :root {
    --ink: #2b2b2b;
    --brand: #2e2a8c;
    --accent: #e0195e;
    --white: #ffffff;
    --topline: #12123a;
    --blue-deep: #1d7fb3;
    --blue-mid: #2b8dbf;
    --wall-grey: #869a9b;
  }
  * { box-sizing: border-box; margin: 0; padding: 0; }
  html, body { width: 1200px; height: 497px; overflow: hidden; background: var(--white); }
  body { position: relative; font-family: "Open Sans", sans-serif; }

  .site-header {
    position: absolute; top: 0; left: 0; width: 1200px; height: 66px;
    background: var(--white);
    border-top: 2px solid var(--topline);
    box-shadow: 0 1px 3px rgba(0,0,0,0.12);
    z-index: 2;
  }
  .brand {
    position: absolute; left: 35px; top: 17px;
    display: flex; align-items: center; gap: 7px;
    font-family: "Open Sans", sans-serif; font-weight: 600;
    font-size: 20px; color: var(--brand); letter-spacing: 0.3px;
  }
  .brand-mark { width: 11px; height: 11px; border-radius: 50%; background: var(--brand); }
  .main-nav {
    position: absolute; left: 468px; top: 23px;
    display: flex; gap: 34px;
    font-size: 14px; color: var(--ink);
  }
  .main-nav a { color: inherit; text-decoration: none; padding-bottom: 2px; }
  .main-nav a.is-active { border-bottom: 2px solid var(--ink); }
  .cta {
    position: absolute; left: 967px; top: 16px; width: 188px; height: 34px;
    background: var(--accent); color: var(--white); border-radius: 3px;
    font-size: 14px; display: flex; align-items: center; justify-content: center;
    text-decoration: none;
  }

  .hero {
    position: absolute; top: 66px; left: 0; width: 1200px; height: 431px;
  }
  .hero-image {
    position: absolute; inset: 0;
    background: linear-gradient(90deg, var(--blue-deep) 0%, var(--blue-mid) 55%, #3d8fb4 66%, var(--wall-grey) 76%, var(--wall-grey) 100%);
  }
  .hero-content {
    position: absolute; inset: 0; text-align: center; color: var(--white);
    font-family: "Varela Round", sans-serif;
  }
  .hero-title { position: absolute; top: 156px; width: 100%; font-size: 54px; font-weight: 400; letter-spacing: 0.5px; }
  .hero-tagline { position: absolute; top: 242px; width: 100%; font-size: 19px; line-height: 44px; letter-spacing: 0.3px; }
</style>
</head>
<body>
  <header class="site-header">
    <div class="brand"><span class="brand-mark"></span>BRANDT Maler</div>
    <nav class="main-nav">
      <a href="#" class="is-active">Home</a>
      <a href="#">Unsere Leistung</a>
      <a href="#">Kontakt</a>
    </nav>
    <a class="cta" href="#">Gespräch vereinbaren</a>
  </header>

  <section class="hero">
    <div class="hero-image" role="img" aria-label="Hand mit Farbroller streicht eine Wand in Blau"></div>
    <div class="hero-content">
      <h1 class="hero-title">Brandt Maler</h1>
      <p class="hero-tagline">Unser höchstes Gebot ist es,<br>stets für vollste Zufriedenheit unserer Kunden zu sorgen.</p>
    </div>
  </section>
</body>
</html>
```